Water Delivery Service Website

We are working with BrivoneÉ. They are a water delivery company and in need of a new website design.
Some sites to use for inspiration:
https://www.tesmoracrest.example/home
https://www.plimvarta.example/en/home3
https://www.quelbo.example
https://www.fandorix.example
Thank you for taking the time to consider designing a website for us. We are web developers based in Stockton, CA, USA. Most of our projects go through the same process. Understanding this process may help you win a project with us. We custom-code all of our websites in-house. We don’t have any requirements as to what tools you use for your design, but we prefer Figma files. For any design that we label as four-stars, we send it to the client for review. The client picks the final design they want us to use. Once we complete this process, we will continue to show additional clients all the four-star sites and purchase them later. Your designs will have multiple chances to sell. For better chances of success, we ask that you follow these guidelines.
IMAGES:
If you use any images or icons in the design, we ask that you have a link to the asset so we can purchase the image/icon. Most of the designs we submit do not have the customer’s images on them unless they have some great images. Be creative; show us the feeling you are trying to portray with your image choices. Use any royalty-free site you choose. We subscribe to Adobe and mainly use their images, but we can purchase images outside of Adobe.
PLEASE NOTE: we will not submit designs to clients with watermarks on the images.
FONTS:
We ask that you identify the fonts used in the design. This can be done in a message if you want. We typically use Google Fonts and Adobe Fonts.
CONTENT:
We're always open to different content and ideas. We often submit designs with stock images so the client can see our vision. We typically take pictures after the website launch to use their images with our vision. Lorem Ipsum is fine for paragraphs, but we ask that you write the headers in correct English. We want to be able to show the vision and identify the sections of the website.
INSPIRATION:
We typically add a couple of links in the brief of websites we like to help you get started in your design.
REVISIONS:
We do not often ask for revisions of the designs unless we see something in the design that may not appeal to the client. If there are slight changes that we want to make, we do that in the development process.
FEEDBACK:
We rarely give feedback on designs during the design process. We are working on many website projects and do not have the time to provide feedback. We usually respond if your request is well thought out and asks specific questions, but a note asking “feedback, please” usually goes unanswered.

```html
<!DOCTYPE html>
<html lang="en">
<head>
<meta charset="utf-8">
<title>BrivoneÉ – Water Delivery</title>
<link href="https://fonts.googleapis.com/css2?family=Jost:wght@400;500;600&display=swap" rel="stylesheet">
<style>
:root{
  --blue:#20ace6;
  --blue-dark:#1a95cf;
  --navy:#1d2b6e;
  --ink:#111418;
  --muted:#3b3f45;
  --line:#e3e6ea;
  --white:#ffffff;
  --black:#000000;
  --tint:#e9f6fc;
}
*{box-sizing:border-box;margin:0;padding:0}
html,body{width:1200px;height:4274px;overflow:hidden}
body{position:relative;font-family:'Jost',sans-serif;color:var(--ink);background:var(--white)}
.abs{position:absolute}
.btn{position:absolute;display:flex;align-items:center;justify-content:center;background:var(--blue);color:var(--white);border-radius:20px;font-size:14px;font-weight:500;height:34px}
.h-section{position:absolute;left:0;width:1200px;text-align:center;font-weight:500;font-size:54px;color:var(--ink)}
.sub-center{position:absolute;left:0;width:1200px;text-align:center;font-size:13px;line-height:22px;color:var(--ink)}

/* top bar */
.topbar{top:0;left:0;width:1200px;height:47px;background:var(--blue)}
.pill-out{position:absolute;top:11px;height:25px;border:1.5px solid var(--white);border-radius:13px;color:var(--white);font-size:12px;font-weight:500;display:flex;align-items:center;justify-content:center;gap:6px}

/* nav */
.logo-word{font-weight:500;color:var(--navy);display:flex;align-items:center;gap:8px}
.logo-dot{width:22px;height:22px;border-radius:50%;background:var(--blue)}
.nav-link{position:absolute;top:79px;font-size:14px;font-weight:500}
.nav-icon{position:absolute;top:72px;width:30px;height:30px;border-radius:50%;background:var(--navy);display:flex;align-items:center;justify-content:center}

/* photo areas */
.photo{position:absolute;overflow:hidden}

/* cards */
.card{position:absolute;background:var(--white);border:1px solid var(--line);border-radius:6px;box-shadow:0 2px 10px rgba(0,0,0,.05)}
.card-img{position:absolute;left:10px;right:10px;top:10px;height:220px;border:1px solid var(--line)}
.card-title{position:absolute;left:12px;font-size:15px;font-weight:600}
.card-text{position:absolute;left:12px;right:16px;font-size:12px;line-height:22px;color:var(--muted)}

.about-pill{position:absolute;left:658px;width:480px;height:42px;border:1px solid var(--line);border-radius:21px;display:flex;align-items:center;font-size:14px;font-weight:500;color:var(--navy);padding-left:60px}
.about-pill .ic{position:absolute;left:16px;top:9px}
.about-pill .chev{position:absolute;right:16px;top:15px}

.how-title{position:absolute;font-size:19px;font-weight:600;color:var(--blue)}
.how-text{position:absolute;width:260px;font-size:13px;line-height:22px;color:var(--muted)}
.how-icon{position:absolute;width:94px;height:94px;border-radius:50%;border:1px solid var(--line);background:var(--white);display:flex;align-items:center;justify-content:center}

.stat{position:absolute;left:697px;width:403px;height:120px;background:var(--white)}
.stat b{position:absolute;left:22px;top:18px;font-size:40px;font-weight:500;color:var(--navy)}
.stat span{position:absolute;left:26px;top:76px;font-size:17px;color:var(--muted)}

.arrow-btn{position:absolute;width:40px;height:40px;border-radius:50%;border:1px solid var(--line);display:flex;align-items:center;justify-content:center;background:var(--white)}

.review{position:absolute;top:3122px;width:347px;height:200px;border:1px solid var(--line);border-radius:4px}
.avatar{position:absolute;left:24px;top:22px;width:50px;height:50px;border-radius:50%;background:linear-gradient(135deg,#d9c0ae,#7a5a4c)}
.rev-name{position:absolute;left:88px;top:36px;font-size:14px;font-weight:600}
.stars{position:absolute;right:26px;top:34px;color:#f2b705;font-size:14px;letter-spacing:4px}
.rev-text{position:absolute;left:26px;top:92px;right:26px;font-size:12.5px;line-height:22px;color:var(--muted)}
.rev-date{position:absolute;left:28px;top:168px;font-size:12px;color:var(--muted)}
.rev-more{position:absolute;right:28px;top:168px;font-size:12px;font-weight:500}

.tag{position:absolute;top:228px;height:20px;padding:0 12px;border-radius:10px;background:var(--tint);color:var(--blue);font-size:11px;display:flex;align-items:center}

/* footer */
.footer{top:4000px;left:0;width:1200px;height:274px;background:var(--black);color:var(--white)}
.f-head{position:absolute;top:42px;font-size:15px;color:var(--blue);font-weight:500}
.f-list{position:absolute;top:76px;font-size:12px;line-height:21px}
.f-social{position:absolute;top:145px;width:28px;height:28px;border-radius:50%;background:var(--blue)}
.f-ic{position:absolute;left:933px;width:24px;height:24px;border-radius:50%;background:var(--blue);display:flex;align-items:center;justify-content:center}
.f-ct{position:absolute;left:972px;font-size:12px;line-height:20px}
</style>
</head>
<body>

<!-- top bar -->
<div class="abs topbar">
  <div class="pill-out" style="left:58px;width:88px">Commercial</div>
  <div class="pill-out" style="left:160px;width:86px">Residential</div>
  <div class="pill-out" style="left:963px;width:180px">
    <svg width="10" height="13" viewBox="0 0 10 13"><path d="M5 12S1 7.5 1 5a4 4 0 0 1 8 0c0 2.5-4 7-4 7z" fill="none" stroke="#fff" stroke-width="1.4"/><circle cx="5" cy="5" r="1.4" fill="#fff"/></svg>
    Find a location near me</div>
</div>

<!-- nav -->
<div class="abs logo-word" style="left:58px;top:70px;font-size:28px"><span class="logo-dot"></span>BrivoneÉ</div>
<div class="nav-link" style="left:390px">About</div>
<div class="nav-link" style="left:473px">Product</div>
<div class="nav-link" style="left:563px">How it works</div>
<div class="nav-link" style="left:690px">Water Resources</div>
<div class="nav-link" style="left:842px">Contact</div>
<div class="nav-icon" style="left:1065px"><svg width="16" height="16" viewBox="0 0 16 16"><circle cx="8" cy="8" r="6.5" fill="none" stroke="#fff" stroke-width="1.3"/><path d="M1.5 8h13M8 1.5c2 2 2 11 0 13M8 1.5c-2 2-2 11 0 13" fill="none" stroke="#fff" stroke-width="1.1"/></svg></div>
<div class="nav-icon" style="left:1112px"><svg width="16" height="15" viewBox="0 0 16 15"><path d="M1 1h2.5l2 9h8l1.5-6H4.5" fill="none" stroke="#fff" stroke-width="1.3"/><circle cx="6.5" cy="13" r="1.2" fill="#fff"/><circle cx="12.5" cy="13" r="1.2" fill="#fff"/></svg></div>

<!-- hero -->
<div class="photo" role="img" aria-label="Smiling woman drinking a glass of water in a bright white kitchen" style="left:0;top:126px;width:1200px;height:465px;background:
  radial-gradient(ellipse 160px 230px at 830px 270px,#d9c6a8 0%,rgba(217,198,168,0) 100%),
  radial-gradient(ellipse 260px 200px at 1110px 420px,#c9cdd0 0%,rgba(201,205,208,0) 100%),
  radial-gradient(ellipse 300px 160px at 700px 40px,#e6e6e2 0%,rgba(230,230,226,0) 100%),
  linear-gradient(90deg,#fbfbfa 0%,#f4f4f2 50%,#ebe9e5 75%,#f1f0ee 100%)"></div>
<h1 class="abs" style="left:55px;top:218px;font-size:58px;font-weight:500;line-height:76px">Healthy Hydration,<br>Straight to Your Door</h1>
<p class="abs" style="left:57px;top:390px;width:520px;font-size:13px;line-height:22px">Lorem ipsum dolor sit amet, consectetuer adipiscing elit, sed diam nonummy nibh euismod tincidunt ut laoreet dolore magna aliquam erat volutpat.</p>
<div class="btn" style="left:57px;top:457px;width:148px">Get Pure Water</div>
<div class="abs" style="left:1087px;top:308px;width:58px;height:58px;border-radius:50%;background:var(--navy);display:flex;align-items:center;justify-content:center">
  <svg width="30" height="10" viewBox="0 0 30 10"><path d="M0 5h28M24 1l4 4-4 4" stroke="#fff" stroke-width="1.6" fill="none"/></svg>
</div>

<!-- about -->
<div class="photo" role="img" aria-label="Hand filling a glass under a chrome kitchen faucet beside green plants" style="left:57px;top:650px;width:519px;height:346px;background:
  radial-gradient(ellipse 120px 160px at 40px 80px,#6f9a3c 0%,rgba(111,154,60,0) 100%),
  radial-gradient(ellipse 140px 140px at 480px 60px,#7ea446 0%,rgba(126,164,70,0) 100%),
  radial-gradient(ellipse 200px 120px at 260px 330px,#b9bec2 0%,rgba(185,190,194,0) 100%),
  radial-gradient(ellipse 70px 90px at 340px 200px,#e5d2c4 0%,rgba(229,210,196,0) 100%),
  linear-gradient(135deg,#e9ece6 0%,#f4f5f3 50%,#e1e5e3 100%)"></div>
<h2 class="abs" style="left:660px;top:646px;font-size:56px;font-weight:500">About</h2>
<p class="abs" style="left:658px;top:722px;width:490px;font-size:13px;line-height:22px">Lorem ipsum dolor sit amet, consectetuer adipiscing elit, sed diam nonummy nibh euismod tincidunt ut laoreet dolore magna aliquam erat volutpat.</p>
<div class="about-pill" style="top:783px"><svg class="ic" width="22" height="22" viewBox="0 0 22 22"><path d="M6 3h10l-1 16H7z M6 8h10" fill="none" stroke="#20ace6" stroke-width="1.4"/></svg>Spring Water<svg class="chev" width="8" height="12" viewBox="0 0 8 12"><path d="M2 1l5 5-5 5" stroke="#111" stroke-width="1.5" fill="none"/></svg></div>
<div class="about-pill" style="top:843px"><svg class="ic" width="22" height="22" viewBox="0 0 22 22"><path d="M11 3c-3 4-5 7-5 10a5 5 0 0 0 10 0c0-3-2-6-5-10z" fill="none" stroke="#20ace6" stroke-width="1.4"/></svg>Purified Water<svg class="chev" width="8" height="12" viewBox="0 0 8 12"><path d="M2 1l5 5-5 5" stroke="#111" stroke-width="1.5" fill="none"/></svg></div>
<div class="about-pill" style="top:901px"><svg class="ic" width="22" height="22" viewBox="0 0 22 22"><path d="M9 2h4v3l2 2v13H7V7l2-2z M7 12h8" fill="none" stroke="#20ace6" stroke-width="1.4"/></svg>Distilled Water<svg class="chev" width="8" height="12" viewBox="0 0 8 12"><path d="M2 1l5 5-5 5" stroke="#111" stroke-width="1.5" fill="none"/></svg></div>
<div class="btn" style="left:658px;top:967px;width:120px">Learn More</div>

<!-- product -->
<h2 class="h-section" style="top:1084px">Product</h2>
<div class="photo" role="img" aria-label="Clear blue water seen from just below a splashing surface" style="left:0;top:1160px;width:1200px;height:536px;background:
  radial-gradient(ellipse 600px 60px at 600px 40px,rgba(255,255,255,.9) 0%,rgba(255,255,255,0) 100%),
  radial-gradient(ellipse 300px 200px at 150px 350px,#8fd2f1 0%,rgba(143,210,241,0) 100%),
  radial-gradient(ellipse 300px 200px at 1050px 330px,#1f8fd1 0%,rgba(31,143,209,0) 100%),
  linear-gradient(180deg,#ffffff 0%,#bfe4f5 9%,#5cbbe6 25%,#3aa6df 55%,#6cc3ec 85%,#a8dcf4 100%)"></div>
<p class="sub-center" style="top:1170px">Lorem ipsum dolor sit amet, consectetuer adipiscing elit, sed diam nonummy nibh<br>euismod tincidunt ut laoreet dolore magna aliquam erat volutpat.</p>

<div class="card" style="left:57px;top:1250px;width:354px;height:388px">
  <div class="card-img" role="img" aria-label="Water filter housings, cartridges and a softener tank" style="background:
    radial-gradient(ellipse 40px 60px at 95px 70px,#3a3d42 0%,rgba(58,61,66,0) 100%),
    radial-gradient(ellipse 70px 40px at 210px 70px,#e6e8ea 0%,rgba(230,232,234,0) 100%),
    radial-gradient(ellipse 60px 45px at 100px 175px,#2c2f33 0%,rgba(44,47,51,0) 100%),
    radial-gradient(ellipse 55px 40px at 180px 175px,#34373b 0%,rgba(52,55,59,0) 100%),
    #fafafa"></div>
  <div class="card-title" style="top:256px">Accessories</div>
  <div class="card-text" style="top:284px">diam nonummy nibh euismod tincidunt ut laoreet dolore magna aliquam erat volutpat.</div>
  <div class="btn" style="left:12px;top:342px;width:110px">Shop Now</div>
</div>
<div class="card" style="left:422px;top:1250px;width:355px;height:388px">
  <div class="card-img" role="img" aria-label="Glass being filled at a dark kitchen faucet" style="background:
    radial-gradient(ellipse 60px 80px at 40px 60px,#5d7a48 0%,rgba(93,122,72,0) 100%),
    radial-gradient(ellipse 90px 120px at 250px 100px,#5a5c5e 0%,rgba(90,92,94,0) 100%),
    radial-gradient(ellipse 50px 60px at 160px 150px,#eef3f6 0%,rgba(238,243,246,0) 100%),
    radial-gradient(ellipse 80px 40px at 100px 160px,#d9b7a2 0%,rgba(217,183,162,0) 100%),
    linear-gradient(135deg,#a9ada8,#d7d8d4 60%,#9ea19e)"></div>
  <div class="card-title" style="top:256px">Pure Water</div>
  <div class="card-text" style="top:284px">diam nonummy nibh euismod tincidunt ut laoreet dolore magna aliquam erat volutpat.</div>
  <div class="btn" style="left:12px;top:342px;width:110px">Shop Now</div>
</div>
<div class="card" style="left:788px;top:1250px;width:355px;height:388px">
  <div class="card-img" role="img" aria-label="Black floor-standing water dispenser" style="background:
    radial-gradient(ellipse 32px 110px at 167px 110px,#202327 0%,#2b2e33 70%,rgba(43,46,51,0) 100%),
    #fafafa"></div>
  <div class="card-title" style="top:256px">Dispensers</div>
  <div class="card-text" style="top:284px">diam nonummy nibh euismod tincidunt ut laoreet dolore magna aliquam erat volutpat.</div>
  <div class="btn" style="left:12px;top:342px;width:110px">Shop Now</div>
</div>

<!-- how it works -->
<h2 class="h-section" style="top:1778px">How it works</h2>
<p class="sub-center" style="top:1858px">Lorem ipsum dolor sit amet, consectetuer adipiscing elit, sed diam nonummy nibh<br>euismod tincidunt ut laoreet dolore magna aliquam erat volutpat.</p>

<div class="how-title" style="left:73px;top:1966px">Better Taste</div>
<div class="how-text" style="left:74px;top:1998px">Lorem ipsum dolor sit amet, consectetuer adipiscing elit, sed diam non volutpat.</div>
<div class="how-icon" style="left:349px;top:1958px"><svg width="40" height="40" viewBox="0 0 40 40"><path d="M12 6h16l-2 28H14z M13 14h14" fill="none" stroke="#20ace6" stroke-width="1.6"/><path d="M20 20c-2 3-3 4-3 5.5a3 3 0 0 0 6 0c0-1.5-1-2.5-3-5.5z" fill="#20ace6"/></svg></div>

<div class="how-title" style="left:880px;top:1969px">Healthier Water</div>
<div class="how-text" style="left:882px;top:2004px">Lorem ipsum dolor sit amet, consectetuer adipiscing elit, sed diam non volutpat.</div>
<div class="how-icon" style="left:758px;top:1958px"><svg width="40" height="40" viewBox="0 0 40 40"><path d="M6 14h20v8H6zM26 18h6v10M14 10h8" fill="none" stroke="#20ace6" stroke-width="1.6"/><path d="M32 32c-1.5 2-2 3-2 4a2 2 0 0 0 4 0c0-1-.5-2-2-4z" fill="#20ace6"/></svg></div>

<div class="photo" role="img" aria-label="Large blue water jug with a bottle and a glass of water" style="left:500px;top:1985px;width:230px;height:300px;background:
  radial-gradient(ellipse 75px 120px at 85px 150px,#5a9bdc 0%,#8ec0ec 60%,rgba(142,192,236,0) 100%),
  radial-gradient(ellipse 20px 30px at 85px 20px,#2a6fc0 0%,rgba(42,111,192,0) 100%),
  radial-gradient(ellipse 20px 70px at 140px 220px,#dcebf6 0%,rgba(220,235,246,0) 100%),
  radial-gradient(ellipse 25px 40px at 190px 250px,#cfe4f4 0%,rgba(207,228,244,0) 100%),
  #ffffff"></div>

<div class="how-title" style="left:68px;top:2190px">Get water delivery</div>
<div class="how-text" style="left:68px;top:2222px">Lorem ipsum dolor sit amet, consectetuer adipiscing elit, sed diam non volutpat.</div>
<div class="how-icon" style="left:366px;top:2180px"><svg width="44" height="34" viewBox="0 0 44 34"><path d="M2 6h26v20H2zM28 12h8l6 7v7H28z" fill="none" stroke="#20ace6" stroke-width="1.6"/><circle cx="10" cy="28" r="3.5" fill="#fff" stroke="#20ace6" stroke-width="1.6"/><circle cx="34" cy="28" r="3.5" fill="#fff" stroke="#20ace6" stroke-width="1.6"/></svg></div>

<div class="how-title" style="left:880px;top:2180px">Sustainable Solutions</div>
<div class="how-text" style="left:882px;top:2212px">Lorem ipsum dolor sit amet, consectetuer adipiscing elit, sed diam non volutpat.</div>
<div class="how-icon" style="left:758px;top:2180px"><svg width="40" height="40" viewBox="0 0 40 40"><circle cx="20" cy="20" r="15" fill="none" stroke="#20ace6" stroke-width="1.6"/><path d="M8 14c5 2 7 6 5 10M25 6c-2 5 2 8 7 8M20 35c0-5 4-8 9-7" fill="none" stroke="#20ace6" stroke-width="1.6"/></svg></div>

<!-- delivery band -->
<svg class="abs" style="left:0;top:2430px" width="1200" height="510" viewBox="0 0 1200 510" aria-hidden="true">
  <path d="M0 50 C200 0 360 90 560 40 C760 -10 960 20 1200 25 L1200 440 C1000 430 820 480 600 470 C380 460 200 520 0 490 Z" fill="#20ace6"/>
  <path d="M0 60 C220 20 380 80 560 45 C720 15 900 20 1050 45" fill="none" stroke="#1a95cf" stroke-width="3"/>
  <path d="M700 470 C850 440 1000 410 1200 430 L1200 445 C1000 435 860 470 700 470Z" fill="#7fd0f2"/>
</svg>
<div class="photo" role="img" aria-label="Faint world map" style="left:610px;top:2520px;width:540px;height:290px;background:radial-gradient(ellipse at center,#4fc0ee 0%,rgba(32,172,230,0) 70%)"></div>
<h2 class="abs" style="left:68px;top:2572px;font-size:56px;font-weight:500;line-height:80px;color:var(--white)">Get High-Quality<br>Water Delivered</h2>
<p class="abs" style="left:70px;top:2734px;font-size:28px;color:var(--navy)">For Anyone, Anywhere.</p>
<div class="btn" style="left:69px;top:2798px;width:155px;background:var(--white);color:var(--blue)">Get water delivery</div>
<div class="stat" style="top:2511px"><b>169M</b><span>customers worldwide</span></div>
<div class="stat" style="top:2649px"><b>56+</b><span>Brands globally and counting</span></div>

<!-- reviews -->
<h2 class="h-section" style="top:2996px">Customer Review</h2>
<div class="arrow-btn" style="left:1053px;top:3013px"><svg width="16" height="10" viewBox="0 0 16 10"><path d="M16 5H2M6 1L2 5l4 4" stroke="#111" stroke-width="1.5" fill="none"/></svg></div>
<div class="arrow-btn" style="left:1102px;top:3013px"><svg width="16" height="10" viewBox="0 0 16 10"><path d="M0 5h14M10 1l4 4-4 4" stroke="#111" stroke-width="1.5" fill="none"/></svg></div>

<div class="review" style="left:62px"><div class="avatar" role="img" aria-label="Customer portrait"></div><div class="rev-name">Mirela Tossani</div><div class="stars">★★★★</div><div class="rev-text">Lorem ipsum dolor sit amet, consectetuer adipiscing elit, sed diam non volutpat.</div><div class="rev-date">06/04/2022</div><div class="rev-more">Read More</div></div>
<div class="review" style="left:426px"><div class="avatar" role="img" aria-label="Customer portrait"></div><div class="rev-name">Garrick Hollen</div><div class="stars">★★★★</div><div class="rev-text">Lorem ipsum dolor sit amet, consectetuer adipiscing elit, sed diam non volutpat.</div><div class="rev-date">15/07/2023</div><div class="rev-more">Read More</div></div>
<div class="review" style="left:790px"><div class="avatar" role="img" aria-label="Customer portrait"></div><div class="rev-name">Veda Marsoli</div><div class="stars">★★★★</div><div class="rev-text">Lorem ipsum dolor sit amet, consectetuer adipiscing elit, sed diam non volutpat.</div><div class="rev-date">26/04/2024</div><div class="rev-more">Read More</div></div>

<!-- blogs -->
<h2 class="h-section" style="top:3396px">Blogs</h2>
<div class="arrow-btn" style="left:1053px;top:3415px"><svg width="16" height="10" viewBox="0 0 16 10"><path d="M16 5H2M6 1L2 5l4 4" stroke="#111" stroke-width="1.5" fill="none"/></svg></div>
<div class="arrow-btn" style="left:1102px;top:3415px"><svg width="16" height="10" viewBox="0 0 16 10"><path d="M0 5h14M10 1l4 4-4 4" stroke="#111" stroke-width="1.5" fill="none"/></svg></div>

<div class="card" style="left:57px;top:3500px;width:354px;height:450px">
  <div class="card-img" role="img" aria-label="Fresh vegetables being rinsed in a kitchen sink" style="height:212px;background:
    radial-gradient(ellipse 60px 50px at 190px 100px,#4f7d2e 0%,rgba(79,125,46,0) 100%),
    radial-gradient(ellipse 50px 40px at 290px 60px,#d9632a 0%,rgba(217,99,42,0) 100%),
    radial-gradient(ellipse 60px 40px at 90px 180px,#c83a22 0%,rgba(200,58,34,0) 100%),
    radial-gradient(ellipse 80px 60px at 60px 50px,#ece8e2 0%,rgba(236,232,226,0) 100%),
    linear-gradient(180deg,#8d8a84 0%,#5c5a55 100%)"></div>
  <div class="tag" style="left:12px">News</div><div class="tag" style="right:12px">Read 6Mins</div>
  <div class="card-title" style="top:270px;font-size:18px;font-weight:500">Mineral Water</div>
  <div class="card-text" style="top:304px;font-size:12.5px">Lorem ipsum dolor sit amet, consectetuer adipiscing elit, sed diam nonummy nibh euismod tincidunt</div>
  <div class="btn" style="left:12px;top:402px;width:112px">Read More</div>
</div>
<div class="card" style="left:422px;top:3500px;width:355px;height:450px">
  <div class="card-img" role="img" aria-label="Still water surface beside a dark wooden fence" style="height:212px;background:linear-gradient(180deg,#2e2624 0%,#4a3c38 40%,#6b5d57 55%,#9aa0a6 72%,#c3c9ce 100%)"></div>
  <div class="tag" style="left:12px">Events</div><div class="tag" style="right:12px">Read 6Mins</div>
  <div class="card-title" style="top:270px;font-size:18px;font-weight:500">Spring Water</div>
  <div class="card-text" style="top:304px;font-size:12.5px">Lorem ipsum dolor sit amet, consectetuer adipiscing elit, sed diam nonummy nibh euismod tincidunt</div>
  <div class="btn" style="left:12px;top:402px;width:112px">Read More</div>
</div>
<div class="card" style="left:788px;top:3500px;width:355px;height:450px">
  <div class="card-img" role="img" aria-label="Glass being filled at a dark kitchen faucet" style="height:212px;background:
    radial-gradient(ellipse 60px 80px at 40px 60px,#5d7a48 0%,rgba(93,122,72,0) 100%),
    radial-gradient(ellipse 90px 110px at 250px 90px,#5a5c5e 0%,rgba(90,92,94,0) 100%),
    radial-gradient(ellipse 50px 60px at 160px 145px,#eef3f6 0%,rgba(238,243,246,0) 100%),
    radial-gradient(ellipse 80px 40px at 100px 155px,#d9b7a2 0%,rgba(217,183,162,0) 100%),
    linear-gradient(135deg,#a9ada8,#d7d8d4 60%,#9ea19e)"></div>
  <div class="tag" style="left:12px">News</div><div class="tag" style="right:12px">Read 6Mins</div>
  <div class="card-title" style="top:266px;font-size:18px;font-weight:500">Drinking Water</div>
  <div class="card-text" style="top:300px;font-size:12.5px">Lorem ipsum dolor sit amet, consectetuer adipiscing elit, sed diam nonummy nibh euismod tincidunt</div>
  <div class="btn" style="left:12px;top:402px;width:112px">Read More</div>
</div>

<!-- footer -->
<footer class="abs footer">
  <div class="abs logo-word" style="left:58px;top:62px;font-size:36px;color:var(--white)"><span class="logo-dot" style="width:28px;height:28px"></span>BrivoneÉ</div>
  <div class="f-social" style="left:60px"></div>
  <div class="f-social" style="left:99px"></div>
  <div class="f-social" style="left:138px"></div>
  <div class="f-social" style="left:178px"></div>

  <div class="f-head" style="left:476px">Quicklinks</div>
  <div class="f-list" style="left:476px">Home<br>About<br>Product<br>Water Resources<br>Contact</div>
  <div class="f-head" style="left:716px">Products</div>
  <div class="f-list" style="left:716px">Dispensers<br>Water<br>Accessories</div>
  <div class="f-head" style="left:933px">Contact</div>
  <div class="f-ic" style="top:80px"><svg width="12" height="12" viewBox="0 0 12 12"><path d="M2 1h2l1 3-1.5 1a7 7 0 0 0 3.5 3.5L8 7l3 1v2a1 1 0 0 1-1 1A9 9 0 0 1 1 2a1 1 0 0 1 1-1z" fill="#fff"/></svg></div><div class="f-ct" style="top:82px">02900415827</div>
  <div class="f-ic" style="top:112px"><svg width="10" height="13" viewBox="0 0 10 13"><path d="M5 12S1 7.5 1 5a4 4 0 0 1 8 0c0 2.5-4 7-4 7z" fill="#fff"/><circle cx="5" cy="5" r="1.4" fill="#20ace6"/></svg></div><div class="f-ct" style="top:106px">Lorem ipsum dolor sit amet,<br>consectetuer adipiscing elit</div>
  <div class="f-ic" style="top:157px"><svg width="12" height="9" viewBox="0 0 12 9"><rect x="0.5" y="0.5" width="11" height="8" fill="#fff"/><path d="M0.5 0.5l5.5 4.5 5.5-4.5" fill="none" stroke="#20ace6" stroke-width="1"/></svg></div><div class="f-ct" style="top:159px">info@brivonee.example</div>

  <div class="abs" style="left:0;top:218px;width:1200px;height:1px;background:#333"></div>
  <div class="abs" style="left:57px;top:236px;font-size:12px">© brivonee 2025 all rights reserved</div>
  <div class="abs" style="right:60px;top:238px;font-size:12px">Terms &amp; Conditions</div>
</footer>

</body>
</html>
```